Webdesign für Immobilienmakler / Immobilienbüro
Zielgruppe
Das Unternehmen heißt LUMAR GmbH und kommt aus Heerbrugg in der Schweiz und will nun den Bereich Immobilien Vermarktung, Verkauf, Vermietung auf Süddeutschland erweitern.
Wir haben bis heute keine Webseite, weil unser Geschäft bis dato in der Schweiz durch Empfehlung, Mundpropaganda und Zeitunganzeigen funktioniert hat. Aber in Deutschland ist es ja ein Muß, was uns sicherlich auch den Einstieg erleichtern wird.
Aufgabenstellung
Wir benötigen eine Homepage für den Verkauf, Vermietung, Vermittlung von Immobilien für Privat und Gewerbe. Zu den Kategorien und der Gliederung haben wir keine bestimmte Vorstellung.
Hier hat der Designer freie Hand und wir freuen uns auf Ihren Vorschlag

```html
<!DOCTYPE html>
<html lang="de">
<head>
<meta charset="utf-8">
<title>LUMAR GmbH – Immobilien</title>
<link rel="stylesheet" href="https://fonts.googleapis.com/css2?family=Open+Sans:wght@400;600;700;800&display=swap">
<style>
:root{
  --red:#c4122a;
  --red-dark:#9e0d20;
  --ink:#1f1e20;
  --text:#444;
  --muted:#666;
  --page:#ececec;
  --white:#fff;
}
*{box-sizing:border-box;margin:0;padding:0}
html,body{width:1160px;height:1200px;overflow:hidden}
body{position:relative;font-family:"Open Sans",Arial,sans-serif;color:var(--text);
  background:radial-gradient(ellipse at 50% 40%,#fafafa 0%,var(--page) 70%)}
.abs{position:absolute}

/* hero */
.hero-photo{left:0;top:0;width:1160px;height:451px;
  background:linear-gradient(180deg,#cfd8e4 0%,#c7b3a4 30%,#b8a090 55%,#9c7f6c 75%,#6f8a46 88%,#54752f 100%)}
.header-band{left:0;top:0;width:1160px;height:110px;background:rgba(255,255,255,.82)}
.brand{left:207px;top:18px;font-size:29px;font-weight:800;color:var(--red);letter-spacing:.3px}
.hotline{left:723px;top:0;width:226px;height:63px;background:var(--red);color:var(--white);text-align:center;padding-top:7px}
.hotline small{display:block;font-size:13px;font-weight:400}
.hotline strong{display:block;font-size:23px;font-weight:700;letter-spacing:1px;line-height:28px}
.main-nav{left:206px;top:87px;width:743px;height:38px;background:var(--ink);display:flex;align-items:center;padding-left:17px}
.main-nav a{color:var(--white);text-decoration:none;font-size:16px;margin-right:32px}
.social{position:absolute;right:9px;top:8px;display:flex;gap:7px}
.social span{width:23px;height:23px;background:var(--white);border-radius:3px}

.caption{left:0;top:451px;width:1160px;height:53px;background:var(--white);display:flex;justify-content:center;align-items:center;font-size:16px;color:#555}
.caption .sep{margin:0 11px;color:#999}
.caption a{color:var(--red);font-weight:600;font-style:italic;text-decoration:underline}
.caption .arrow{position:absolute;top:14px}

/* search */
.search{left:207px;top:537px;width:464px;height:195px;background:var(--ink);color:var(--white);font-size:11px}
.search h2{position:absolute;left:17px;top:17px;font-size:18px;font-weight:400}
.search label{position:absolute}
.search .field{position:absolute;background:linear-gradient(#fff,#e9e9e9);border:1px solid #ccc}
.check{display:inline-flex;align-items:center;margin-left:10px}
.check i{width:10px;height:10px;background:#ddd;margin-right:5px;display:inline-block}
.drop{position:absolute;right:0;top:0;height:100%;background:var(--red);display:flex;align-items:center;justify-content:center}
.search-btn{position:absolute;left:452px;top:686px;width:0}
.btn{position:absolute;left:245px;top:149px;width:129px;height:25px;background:var(--red);color:var(--white);font-size:14px;font-weight:600;display:flex;align-items:center;justify-content:center;gap:8px}

.services{left:671px;top:537px;width:279px;height:195px}
.service{position:relative;height:65px;background:linear-gradient(#fdfdfd,#ededed);border-bottom:1px solid #ddd;padding:17px 0 0 13px}
.service h3{font-size:18px;font-weight:400;color:#333;line-height:20px}
.service p{font-size:10px;color:var(--muted)}
.service .go{position:absolute;right:0;top:0;width:23px;height:100%;background:var(--red);display:flex;align-items:center;justify-content:center}
.panel-shadow{left:215px;top:732px;width:730px;height:20px;background:radial-gradient(ellipse at 50% 0,rgba(0,0,0,.28),rgba(0,0,0,0) 70%)}

/* content */
.col h2{font-size:18px;font-weight:400;color:#333;margin-bottom:12px}
.col p{font-size:11.4px;line-height:17px;color:var(--text)}
.col .date,.col .more{color:var(--red);font-weight:600}
.intro{left:208px;top:762px;width:448px}
.news{left:670px;top:762px;width:280px}
.top-title{left:205px;top:922px;font-size:18px;color:#333}

.carousel{left:206px;top:966px;width:744px;height:100px;background:var(--white);box-shadow:0 2px 4px rgba(0,0,0,.15)}
.carousel .nav{position:absolute;top:0;width:24px;height:100%;background:var(--red);display:flex;align-items:center;justify-content:center}
.obj{position:absolute;top:20px;display:flex;gap:16px;font-size:11.5px;line-height:18px;color:#444}
.obj .thumb{width:64px;height:64px}
.obj .more{color:var(--red);font-weight:600}
.divider{position:absolute;top:14px;width:1px;height:72px;background:#e2e2e2}

.site-footer{left:0;top:1097px;width:1160px;height:103px;background:var(--ink);color:var(--white);font-size:12px;line-height:19px}
.site-footer .addr{position:absolute;left:208px;top:11px}
.site-footer .addr strong{display:block;margin-bottom:3px}
.site-footer .legal{position:absolute;right:210px;top:11px;text-align:right}
.site-footer .legal nav a{color:var(--white);text-decoration:none;font-weight:600;margin-left:12px}
.site-footer .legal p{margin-top:6px}
</style>
</head>
<body>

<div class="abs hero-photo" role="img" aria-label="Foto eines großen Einfamilienhauses mit Klinkerfassade und Rasen"></div>
<div class="abs header-band"></div>
<div class="abs brand">LUMAR GmbH</div>
<div class="abs hotline"><small>Wir helfen Ihnen gerne weiter!</small><strong>0361 48290517</strong></div>
<nav class="abs main-nav">
  <a href="#">Über uns</a><a href="#">Immobilien</a><a href="#">Kontakt</a><a href="#">Karriere</a>
  <div class="social"><span></span><span></span><span></span><span></span></div>
</nav>

<div class="abs caption">
  <svg class="arrow" style="left:212px" width="22" height="24" viewBox="0 0 22 24"><path d="M19 3 3 12l16 9" fill="none" stroke="#222" stroke-width="3"/></svg>
  Immobilie in München<span class="sep">|</span>BJ 1995<span class="sep">|</span>Größe 300m²<span class="sep">|</span><a href="#">weitere Informationen</a>
  <svg class="arrow" style="left:924px" width="22" height="24" viewBox="0 0 22 24"><path d="M3 3l16 9-16 9" fill="none" stroke="#222" stroke-width="3"/></svg>
</div>

<section class="abs search">
  <h2>Immobiliensuche</h2>
  <div style="position:absolute;left:305px;top:26px;font-size:11px">
    <span class="check"><i></i>Kaufen</span><span class="check"><i></i>Mieten</span><span class="check"><i></i>Pachten</span>
  </div>
  <label style="left:19px;top:61px"><b>Wo:</b> Ort, PLZ oder Straße</label>
  <label style="left:245px;top:61px"><b>Was:</b> Eigentumswohnung, Haus etc.</label>
  <div class="field" style="left:19px;top:85px;width:201px;height:25px"></div>
  <div class="field" style="left:245px;top:85px;width:201px;height:25px"><span class="drop" style="width:26px"><svg width="12" height="7"><path d="M0 0h12L6 7z" fill="#fff"/></svg></span></div>
  <label style="left:19px;top:128px">Preis bis</label>
  <label style="left:93px;top:128px">Zimmer ab:</label>
  <label style="left:165px;top:128px">Fläche ab:</label>
  <div class="field" style="left:19px;top:149px;width:54px;height:25px"></div>
  <div class="field" style="left:92px;top:149px;width:55px;height:25px"><span class="drop" style="width:17px"><svg width="9" height="5"><path d="M0 0h9L4.5 5z" fill="#fff"/></svg></span></div>
  <div class="field" style="left:164px;top:149px;width:54px;height:25px"></div>
  <div class="btn">Suche starten <svg width="6" height="10"><path d="M0 0l6 5-6 5z" fill="#fff"/></svg></div>
</section>

<div class="abs services">
  <div class="service"><h3>Vermieten</h3><p>Wohnungen, Häuser, Büros, Grundstücke, u.v.m.</p><span class="go"><svg width="6" height="10"><path d="M0 0l6 5-6 5z" fill="#fff"/></svg></span></div>
  <div class="service"><h3>Verkaufen</h3><p>Wohnungen, Häuser, Büros, Grundstücke, u.v.m.</p><span class="go"><svg width="6" height="10"><path d="M0 0l6 5-6 5z" fill="#fff"/></svg></span></div>
  <div class="service"><h3>Vermitteln</h3><p>Neubau, Altbau, Gärten u.v.m.</p><span class="go"><svg width="6" height="10"><path d="M0 0l6 5-6 5z" fill="#fff"/></svg></span></div>
</div>
<div class="abs panel-shadow"></div>

<div class="abs col intro">
  <h2>Finden Sie Ihre Traum Immobilie!</h2>
  <p>Lorem ipsum dolor sit amet, consectetuer adipiscing elit. Aenean commodo ligula eget dolor. Aenean massa. Cum sociis natoque penatibus et magnis dis parturient montes, nascetur ridiculus mus. Donec quam felis, ultricies nec, pellentesque eu, pretium quis, sem. Nulla consequat massa quis enim. Donec pede justo, fringilla vel, aliquet nec, vulputate eget, arcu. In enim justo, rhoncus ut, imperdiet a, venenatis vitae, justo. Nullam dictum felis eu pede mollis pretium. Integer tincidunt.</p>
</div>
<div class="abs col news">
  <h2>News &amp; Aktuelles</h2>
  <p><span class="date">22.01.2013</span> | Lorem ipsum dolor sit amet, consectetuer adipiscing elit. Aenean commodo ligula eget dolor. Aenean massa. Cum sociis natoque penatibus et magnis dis parturient montes, nascetur ridiculus mus. Donec quam felis, ultricies nec, pellentesque eu, pretium quis, sem | <span class="more">mehr erfahren...</span></p>
</div>

<h2 class="abs top-title" style="font-weight:400">Unsere Top-Objekte</h2>
<div class="abs carousel">
  <span class="nav" style="left:0"><svg width="14" height="14"><circle cx="7" cy="7" r="7" fill="#fff"/><path d="M8.5 3.5 5 7l3.5 3.5" fill="none" stroke="#c4122a" stroke-width="2"/></svg></span>
  <div class="obj" style="left:51px">
    <div class="thumb" role="img" aria-label="Foto eines gelben Einfamilienhauses" style="background:linear-gradient(#a9c8e8 0 40%,#e7c95a 40% 80%,#5c8a3a 80%)"></div>
    <div>Art: Einfamilienhaus<br>Ort: Dresden<br>BJ: Mai 2008<br><span class="more">mehr erfahren...</span></div>
  </div>
  <span class="divider" style="left:252px"></span>
  <div class="obj" style="left:276px">
    <div class="thumb" role="img" aria-label="Foto eines modernen weißen Mehrfamilienhauses" style="background:linear-gradient(#5f95d0 0 35%,#eeeeee 35% 70%,#6c7c5a 70%)"></div>
    <div>Art: Mehrfamilienhaus<br>Ort: Köln<br>BJ: November 1996<br><span class="more">mehr erfahren...</span></div>
  </div>
  <span class="divider" style="left:494px"></span>
  <div class="obj" style="left:518px">
    <div class="thumb" role="img" aria-label="Foto einer gläsernen Bürofassade" style="background:linear-gradient(90deg,#3c4a58,#9fb4c8 50%,#6f7f90)"></div>
    <div>Art: Bürogebäude<br>Ort: Frankfurt<br>BJ: August 2009<br><span class="more">mehr erfahren...</span></div>
  </div>
  <span class="nav" style="right:0"><svg width="14" height="14"><circle cx="7" cy="7" r="7" fill="#fff"/><path d="M5.5 3.5 9 7l-3.5 3.5" fill="none" stroke="#c4122a" stroke-width="2"/></svg></span>
</div>

<footer class="abs site-footer">
  <div class="addr">
    <strong>LUMAR GmbH</strong>
    Musterstraße 1 &nbsp;|&nbsp; 00000 Musterstadt<br>
    Tel 0457 2219 3380 &nbsp;|&nbsp; Fax 0457 2219 3381<br>
    info@lumar-immo.de &nbsp;|&nbsp; www.lumar-immo.de
  </div>
  <div class="legal">
    <nav><a href="#">AGB</a><a href="#">Kontakt</a><a href="#">Impressum</a></nav>
    <p>Copyright 2013. All Rights Reserved.</p>
  </div>
</footer>

</body>
</html>
```